Brand-new Pediatric Dental Practice needs a website

We are a brand-new dental practice that will specialize in treating children. We want a gorgeous and easily navigable dental practice website that would make a good first impression to potential patients and their parents. It should be modern, SEO-friendly, mobile responsive, and optimized to win new patients.

Target Market(s)

Parents

Industry/Entity Type

Healthcare/Dentistry

Coding

Coded - Design and coding required

Number of Pages Required

4 page

Requirements
Must have
• Use the Wix website building platform. 4 pages: home, meet our dentists, services, contact us
Nice to have
• has a link to our facebook, instagram

```html
<!DOCTYPE html>
<html lang="en">
<head>
<meta charset="utf-8">
<title>Birch Grove Pediatric Dentistry</title>
<link href="https://fonts.googleapis.com/css2?family=Nunito+Sans:wght@400;600;700;800&display=swap" rel="stylesheet">
<style>
:root{
  --green:#3b9c55;
  --green-dark:#2f8a48;
  --green-light:#b6dcb1;
  --green-pale:#e4f2e0;
  --ink:#3c3c3e;
  --text:#4a4a4a;
  --charcoal:#424244;
  --white:#ffffff;
}
*{margin:0;padding:0;box-sizing:border-box}
html,body{width:1200px;height:5277px;overflow:hidden}
body{position:relative;background:var(--white);font-family:"Nunito Sans",Arial,sans-serif;color:var(--text)}
.abs{position:absolute}
svg.defs{position:absolute;width:0;height:0}

/* header */
.site-header{left:0;top:0;width:1200px;height:118px;border-bottom:1px solid #ddd}
.brand{left:0;width:1200px;top:18px;text-align:center}
.brand-dot{display:block;width:46px;height:46px;border-radius:50%;background:var(--green);margin:0 auto 6px}
.brand-name{font-size:26px;font-weight:700;color:var(--ink);letter-spacing:.5px;line-height:1}
.login{left:955px;top:44px;display:flex;align-items:center;gap:14px;font-size:14px;color:var(--ink)}
.main-nav{left:0;top:118px;width:1200px;height:46px;border-bottom:1px solid #ddd}
.main-nav a{position:absolute;top:14px;font-size:14px;color:var(--ink);text-decoration:none}
.main-nav a.active{color:var(--green)}

/* hero */
.hero{left:0;top:164px;width:1200px;height:570px;background:linear-gradient(100deg,#2f5a22 0%,#4c7a2e 35%,#c99a78 55%,#8a6a3a 75%,#3d6226 100%)}
.hero-title{left:53px;top:422px;font-size:50px;font-weight:800;color:var(--white)}
.hero-sub{left:60px;top:488px;font-size:25px;color:var(--white)}
.btn{display:flex;align-items:center;justify-content:center;border-radius:24px;font-size:15px;font-weight:700;letter-spacing:.3px;text-decoration:none}
.btn-hero{left:129px;top:563px;width:252px;height:45px;background:var(--green);color:var(--white);border:3px solid var(--white)}

/* features */
.features{left:0;top:717px;width:1200px;height:368px;background:var(--green)}
.feature{top:100px;width:260px;color:var(--white)}
.feature-icon{width:70px;height:70px;border:3px solid var(--white);border-radius:50%;margin-bottom:34px}
.feature h3{font-size:22px;font-weight:700;margin-bottom:10px}
.feature p{font-size:14px;line-height:22px}
.feature-divider{top:90px;width:1px;height:190px;background:rgba(255,255,255,.45)}

/* why */
.why-photo{left:162px;top:1192px;width:426px;height:395px;background:linear-gradient(135deg,#5fa0c8,#e7b08e 50%,#cfd9dc)}
.why-title{left:635px;top:1248px;font-size:34px;font-weight:800;color:var(--ink)}
.why-text{left:635px;top:1340px;width:380px;font-size:14.5px;line-height:22.5px}

.section-title{left:0;width:1200px;text-align:center;font-size:34px;font-weight:800;color:var(--ink)}
.divider{left:506px;width:192px;height:4px;display:flex;gap:10px}
.divider span{flex:1;background:var(--green-light)}
.divider span.mid{background:var(--ink)}

/* dentists */
.dentists-band{left:0;top:1962px;width:1200px;height:598px;background:var(--green-light)}
.dentist{top:1794px;width:274px;height:598px}
.dentist-photo{width:274px;height:297px;background:linear-gradient(160deg,#eef1f2,#cfd8dc 60%,#8fb0c0)}
.dentist-body{width:274px;height:301px;background:var(--charcoal);padding:36px 24px 0;color:var(--white);position:relative}
.dentist-role{font-size:13px;color:#cfcfcf}
.dentist-name{font-size:24px;font-weight:700;margin:8px 0 10px}
.dentist-text{font-size:14px;line-height:22px}
.socials{display:flex;gap:10px;margin-top:26px}
.socials span{width:27px;height:27px;border-radius:50%;background:var(--green-light)}
.card-wave{position:absolute;left:0;bottom:-1px;width:274px;height:36px}
.btn-outline{background:var(--white);color:var(--green);border:3px solid var(--green)}
.btn-meet{left:453px;top:2435px;width:295px;height:45px}

/* services */
.service{width:252px}
.service-photo{width:252px;height:172px;position:relative}
.service-photo svg{position:absolute;left:0;bottom:-1px;width:252px;height:30px}
.svc-a{background:linear-gradient(135deg,#1a1a1a,#7a3a3a 50%,#e8e0da)}
.svc-b{background:linear-gradient(135deg,#1e2630,#4a5a6a 55%,#d9dfe4)}
.svc-c{background:linear-gradient(135deg,#d7a48a,#f0ddd0 50%,#8fb4e0)}
.svc-d{background:linear-gradient(135deg,#2a1a12,#b97a55 55%,#3a2a20)}
.service-cat{font-size:14px;color:var(--ink);margin:28px 0 0 18px}
.service-name{font-size:21px;font-weight:700;color:var(--green);margin:6px 0 8px 18px}
.service-text{font-size:13.5px;line-height:22px;margin-left:18px;width:220px}
.btn-services{left:453px;top:3574px;width:295px;height:45px;background:var(--green);color:var(--white);border:3px solid #a9d6a5}

/* reviews */
.review{top:3813px;width:274px}
.quote{font-size:110px;font-weight:800;color:var(--green);line-height:1;height:48px;margin-left:22px;font-family:Georgia,serif}
.review-card{margin-top:-15px;width:274px;height:367px;background:var(--green-pale);padding:42px 24px 0;position:relative}
.review-name{font-size:15px;font-weight:700;color:var(--ink)}
.stars{color:var(--green);font-size:17px;letter-spacing:3px;margin:4px 0 14px}
.review-text{font-size:14px;line-height:22.5px}

/* contact band */
.contact{left:0;top:4280px;width:1200px;height:338px;background:var(--green)}
.hours-panel{left:737px;top:4280px;width:301px;height:338px;background:var(--green-dark)}
.interested{left:162px;top:4370px;font-size:20px;color:#d9eed6}
.contact-title{left:162px;top:4410px;font-size:28px;font-weight:800;color:var(--white);line-height:32px}
.btn-book{left:162px;top:4506px;width:254px;height:45px;background:var(--white);color:var(--ink);border:3px solid #a9d6a5}
.call{left:466px;top:4505px;display:flex;gap:14px;align-items:center;color:var(--white)}
.call-label{font-size:16px;font-weight:700}
.call-num{font-size:18px;font-weight:800}
.hours-title{left:768px;top:4366px;font-size:25px;font-weight:700;color:var(--white)}
.hours-list{left:768px;top:4414px;width:222px;font-size:13px;color:var(--white)}
.hours-list div{height:30px;border-bottom:1px solid rgba(255,255,255,.4);padding-top:4px}
.office-contact{left:768px;top:4524px;font-size:13px;color:var(--white)}
.office-contact div{display:flex;gap:10px;align-items:center;height:30px}

/* footer */
.site-footer{left:0;top:4618px;width:1200px;height:659px;background:var(--charcoal);color:#e2e2e2}
.foot-head{font-size:17px;font-weight:700;color:#9fd49a}
.foot-col{top:118px}
.foot-col p{font-size:13.5px;line-height:22.5px;margin-top:20px;width:380px}
.foot-col ul{list-style:none;margin-top:20px;font-size:13.5px;line-height:22.5px}
.foot-brand{left:0;top:360px;width:1200px;text-align:center}
.foot-brand .brand-dot{width:70px;height:70px;background:#7cc57a;margin-bottom:14px}
.foot-brand .brand-name{color:var(--white);font-size:34px}
.foot-social{left:479px;top:528px;display:flex;gap:17px}
.foot-social span{width:42px;height:42px;border-radius:50%;background:#8ccd87}
.copyright{left:0;top:592px;width:1200px;text-align:center;font-size:14px;color:#e0e0e0}
</style>
</head>
<body>
<svg class="defs" aria-hidden="true">
  <defs>
    <pattern id="wave-green" width="80" height="40" patternUnits="userSpaceOnUse">
      <path d="M0 40 V18 Q20 2 40 18 T80 18 V40 Z" fill="#3b9c55"/>
    </pattern>
    <pattern id="wave-white" width="80" height="40" patternUnits="userSpaceOnUse">
      <path d="M0 40 V18 Q20 2 40 18 T80 18 V40 Z" fill="#ffffff"/>
    </pattern>
    <pattern id="wave-light" width="80" height="40" patternUnits="userSpaceOnUse">
      <path d="M0 40 V18 Q20 2 40 18 T80 18 V40 Z" fill="#b6dcb1"/>
    </pattern>
    <pattern id="wave-card-white" width="68.5" height="36" patternUnits="userSpaceOnUse">
      <path d="M0 36 V20 Q17 0 34 20 T68.5 20 V36 Z" fill="#ffffff"/>
    </pattern>
    <pattern id="wave-card-light" width="68.5" height="36" patternUnits="userSpaceOnUse">
      <path d="M0 36 V20 Q17 0 34 20 T68.5 20 V36 Z" fill="#b6dcb1"/>
    </pattern>
    <pattern id="wave-photo" width="63" height="30" patternUnits="userSpaceOnUse">
      <path d="M0 30 V16 Q16 0 31.5 16 T63 16 V30 Z" fill="#ffffff"/>
    </pattern>
  </defs>
</svg>

<header class="site-header abs">
  <div class="brand abs"><span class="brand-dot"></span><span class="brand-name">birch grove</span></div>
  <div class="login abs">
    <svg width="22" height="22" viewBox="0 0 22 22"><circle cx="11" cy="11" r="10" fill="none" stroke="#3c3c3e" stroke-width="1.6"/><circle cx="11" cy="9" r="3.5" fill="#3c3c3e"/><path d="M4.5 17.5 Q11 11 17.5 17.5" fill="#3c3c3e"/></svg>
    <span>Log In</span>
  </div>
</header>
<nav class="main-nav abs">
  <a class="active" href="#" style="left:390px">Home</a>
  <a href="#" style="left:472px">Meet Our Dentists</a>
  <a href="#" style="left:638px">Services</a>
  <a href="#" style="left:735px">Contact Us</a>
</nav>

<section class="hero abs" role="img" aria-label="Photo of a smiling young girl outdoors on green grass"></section>
<h1 class="hero-title abs">Smiles All Around</h1>
<p class="hero-sub abs">You'll leave our clinicwith a Smile</p>
<a class="btn btn-hero abs" href="#">BOOK APPOINTMENT</a>

<svg class="abs" style="left:0;top:690px" width="1200" height="40"><rect width="1200" height="40" fill="url(#wave-green)"/></svg>
<section class="features abs">
  <div class="feature abs" style="left:170px"><div class="feature-icon"></div><h3>Best Dentists</h3><p>Lorem ipsum dolor sit amet, consectetur adipiscing elit. Aliquam quis semper felis.</p></div>
  <div class="feature-divider abs" style="left:437px"></div>
  <div class="feature abs" style="left:471px"><div class="feature-icon"></div><h3>Quick Examination</h3><p>Lorem ipsum dolor sit amet, consectetur adipiscing elit. Aliquam quis semper felis.</p></div>
  <div class="feature-divider abs" style="left:737px"></div>
  <div class="feature abs" style="left:770px"><div class="feature-icon"></div><h3>Painless Procedures</h3><p>Lorem ipsum dolor sit amet, consectetur adipiscing elit. Aliquam quis semper felis.</p></div>
</section>
<svg class="abs" style="left:0;top:1070px" width="1200" height="40"><rect width="1200" height="40" fill="url(#wave-white)"/></svg>

<div class="why-photo abs" role="img" aria-label="Photo of a boy in sunglasses having his teeth checked in the dental chair"></div>
<svg class="abs" style="left:162px;top:1553px" width="426" height="36"><rect width="426" height="36" fill="url(#wave-card-white)"/></svg>
<h2 class="why-title abs">Why Birch Grove?</h2>
<p class="why-text abs">Lorem ipsum dolor sit amet, consectetur adipiscing elit, sed do eiusmod tempor incididunt ut labore et dolore magna aliqua. Ut enim ad minim veniam, quis nostrud exercitation ullamco laboris nisi ut aliquip ex ea commodo consequat. Duis aute irure dolor in reprehenderit in voluptate velit esse cillum dolore eu fugiat nulla pariatur. Excepteur sint occaecat cupidatat non proident, sunt in culpa qui officia deserunt mollit anim id est laborum.</p>

<h2 class="section-title abs" style="top:1668px">Meet Our Dentists</h2>
<div class="divider abs" style="top:1745px"><span></span><span class="mid"></span><span></span></div>

<div class="dentists-band abs"></div>
<svg class="abs" style="left:0;top:2545px" width="1200" height="40"><rect width="1200" height="40" fill="url(#wave-white)"/></svg>

<article class="dentist abs" style="left:162px">
  <div class="dentist-photo" role="img" aria-label="Portrait photo of a dentist in a white coat"></div>
  <div class="dentist-body"><div class="dentist-role">DENTIST</div><div class="dentist-name">Dentist Name</div><p class="dentist-text">Lorem ipsum dolor sit amet, consectetur adipiscing elit. Aliquam quis semper felis.</p><div class="socials"><span></span><span></span><span></span></div>
  <svg class="card-wave"><rect width="274" height="36" fill="url(#wave-card-light)"/></svg></div>
</article>
<article class="dentist abs" style="left:463px">
  <div class="dentist-photo" role="img" aria-label="Portrait photo of a dentist holding a clipboard"></div>
  <div class="dentist-body"><div class="dentist-role">DENTIST</div><div class="dentist-name">Dentist Name</div><p class="dentist-text">Lorem ipsum dolor sit amet, consectetur adipiscing elit. Aliquam quis semper felis.</p><div class="socials"><span></span><span></span><span></span></div>
  <svg class="card-wave"><rect width="274" height="36" fill="url(#wave-card-light)"/></svg></div>
</article>
<article class="dentist abs" style="left:762px">
  <div class="dentist-photo" role="img" aria-label="Portrait photo of a dentist in blue scrubs"></div>
  <div class="dentist-body"><div class="dentist-role">DENTIST</div><div class="dentist-name">Dentist Name</div><p class="dentist-text">Lorem ipsum dolor sit amet, consectetur adipiscing elit. Aliquam quis semper felis.</p><div class="socials"><span></span><span></span><span></span></div>
  <svg class="card-wave"><rect width="274" height="36" fill="url(#wave-card-light)"/></svg></div>
</article>
<a class="btn btn-outline btn-meet abs" href="#">MEET ALL OUR DENTISTS</a>

<h2 class="section-title abs" style="top:2636px">Our Services</h2>

<article class="service abs" style="left:55px;top:2732px"><div class="service-photo svc-a" role="img" aria-label="Close-up photo of a dental check-up"><svg><rect width="252" height="30" fill="url(#wave-photo)"/></svg></div><div class="service-cat">TEETH</div><div class="service-name">Dental Services</div><p class="service-text">Lorem ipsum dolor sit amet, consectetur adipiscing elit. Maecenas sagittis mi faucibus risus auctor scelerisque.</p></article>
<article class="service abs" style="left:334px;top:2732px"><div class="service-photo svc-b" role="img" aria-label="Photo of a patient under the dental lamp"><svg><rect width="252" height="30" fill="url(#wave-photo)"/></svg></div><div class="service-cat">COSMETIC</div><div class="service-name">Dentistry</div><p class="service-text">Lorem ipsum dolor sit amet, consectetur adipiscing elit. Maecenas sagittis mi faucibus risus auctor scelerisque.</p></article>
<article class="service abs" style="left:612px;top:2732px"><div class="service-photo svc-c" role="img" aria-label="Photo of a child receiving dental treatment"><svg><rect width="252" height="30" fill="url(#wave-photo)"/></svg></div><div class="service-cat">THE BEST SOLUTION</div><div class="service-name">Dental Bridges</div><p class="service-text">Lorem ipsum dolor sit amet, consectetur adipiscing elit. Maecenas sagittis mi faucibus risus auctor scelerisque.</p></article>
<article class="service abs" style="left:891px;top:2732px"><div class="service-photo svc-d" role="img" aria-label="Photo of a laughing child with a bright smile"><svg><rect width="252" height="30" fill="url(#wave-photo)"/></svg></div><div class="service-cat">BEAUTIFY YOUR SMILE</div><div class="service-name">Teeth Whitening</div><p class="service-text">Lorem ipsum dolor sit amet, consectetur adipiscing elit. Maecenas sagittis mi faucibus risus auctor scelerisque.</p></article>

<article class="service abs" style="left:55px;top:3144px"><div class="service-photo svc-a" role="img" aria-label="Close-up photo of a dental check-up"><svg><rect width="252" height="30" fill="url(#wave-photo)"/></svg></div><div class="service-cat">TEETH</div><div class="service-name">Dental Services</div><p class="service-text">Lorem ipsum dolor sit amet, consectetur adipiscing elit. Maecenas sagittis mi faucibus risus auctor scelerisque.</p></article>
<article class="service abs" style="left:334px;top:3144px"><div class="service-photo svc-b" role="img" aria-label="Photo of a patient under the dental lamp"><svg><rect width="252" height="30" fill="url(#wave-photo)"/></svg></div><div class="service-cat">COSMETIC</div><div class="service-name">Dentistry</div><p class="service-text">Lorem ipsum dolor sit amet, consectetur adipiscing elit. Maecenas sagittis mi faucibus risus auctor scelerisque.</p></article>
<article class="service abs" style="left:612px;top:3144px"><div class="service-photo svc-c" role="img" aria-label="Photo of a child receiving dental treatment"><svg><rect width="252" height="30" fill="url(#wave-photo)"/></svg></div><div class="service-cat">THE BEST SOLUTION</div><div class="service-name">Dental Bridges</div><p class="service-text">Lorem ipsum dolor sit amet, consectetur adipiscing elit. Maecenas sagittis mi faucibus risus auctor scelerisque.</p></article>
<article class="service abs" style="left:891px;top:3144px"><div class="service-photo svc-d" role="img" aria-label="Photo of a laughing child with a bright smile"><svg><rect width="252" height="30" fill="url(#wave-photo)"/></svg></div><div class="service-cat">BEAUTIFY YOUR SMILE</div><div class="service-name">Teeth Whitening</div><p class="service-text">Lorem ipsum dolor sit amet, consectetur adipiscing elit. Maecenas sagittis mi faucibus risus auctor scelerisque.</p></article>

<a class="btn btn-services abs" href="#">VIEW ALL OUR SERVICES</a>

<h2 class="section-title abs" style="top:3693px">Patient's Reviews</h2>
<div class="divider abs" style="top:3766px"><span></span><span class="mid"></span><span></span></div>

<article class="review abs" style="left:162px"><div class="quote">&ldquo;</div><div class="review-card"><div class="review-name">Patients Name</div><div class="stars">★★★★★</div><p class="review-text">Lorem ipsum dolor sit amet, consectetur adipiscing elit, sed do eiusmod tempor incididunt ut labore et dolore magna aliqua. Ut enim ad minim veniam, quis nostrud exercitation ullamco laboris nisi ut aliquip ex ea commodo consequat.</p><svg class="card-wave"><rect width="274" height="36" fill="url(#wave-card-white)"/></svg></div></article>
<article class="review abs" style="left:463px"><div class="quote">&ldquo;</div><div class="review-card"><div class="review-name">Patients Name</div><div class="stars">★★★★★</div><p class="review-text">Lorem ipsum dolor sit amet, consectetur adipiscing elit, sed do eiusmod tempor incididunt ut labore et dolore magna aliqua. Ut enim ad minim veniam, quis nostrud exercitation ullamco laboris nisi ut aliquip ex ea commodo consequat.</p><svg class="card-wave"><rect width="274" height="36" fill="url(#wave-card-white)"/></svg></div></article>
<article class="review abs" style="left:762px"><div class="quote">&ldquo;</div><div class="review-card"><div class="review-name">Patients Name</div><div class="stars">★★★★★</div><p class="review-text">Lorem ipsum dolor sit amet, consectetur adipiscing elit, sed do eiusmod tempor incididunt ut labore et dolore magna aliqua. Ut enim ad minim veniam, quis nostrud exercitation ullamco laboris nisi ut aliquip ex ea commodo consequat.</p><svg class="card-wave"><rect width="274" height="36" fill="url(#wave-card-white)"/></svg></div></article>

<svg class="abs" style="left:0;top:4252px" width="1200" height="40"><rect width="1200" height="40" fill="url(#wave-green)"/></svg>
<section class="contact abs"></section>
<div class="hours-panel abs"></div>
<p class="interested abs">Interested?</p>
<h2 class="contact-title abs">CONTACT US AND<br>SCHEDULE YOUR VISIT</h2>
<a class="btn btn-book abs" href="#">BOOK APPOINTMENT</a>
<div class="call abs">
  <svg width="44" height="44" viewBox="0 0 44 44"><circle cx="22" cy="22" r="20" fill="none" stroke="#fff" stroke-width="2"/><path d="M15 13 L19 13 L21 18 L18.5 20 Q21 25 25 26 L27 23.5 L32 25.5 L32 29 Q31 31 28 31 Q16 29 13 17 Q13 14 15 13 Z" fill="none" stroke="#fff" stroke-width="2" stroke-linejoin="round"/></svg>
  <div><div class="call-label">FREE CALL 24/7</div><div class="call-num">+1 555 0142 880</div></div>
</div>
<h3 class="hours-title abs">Office Houres</h3>
<div class="hours-list abs"><div>Monday - Friday : 8am - 8pm</div><div>Saturday : 8am - 6pm</div><div>Sunday : 8am - 6pm</div></div>
<div class="office-contact abs">
  <div><svg width="16" height="18" viewBox="0 0 16 18"><path d="M8 17 Q1 9 1 6.5 A7 7 0 0 1 15 6.5 Q15 9 8 17 Z" fill="#fff"/><circle cx="8" cy="6.5" r="2.5" fill="#2f8a48"/></svg>123 your address details</div>
  <div><svg width="18" height="13" viewBox="0 0 18 13"><rect x="1" y="1" width="16" height="11" fill="none" stroke="#fff" stroke-width="1.5"/><path d="M1 1 L9 7 L17 1" fill="none" stroke="#fff" stroke-width="1.5"/></svg>hello@birchgrove.example</div>
</div>

<footer class="site-footer abs">
  <div class="foot-col abs" style="left:162px"><div class="foot-head">Who We Are</div><p>Lorem ipsum dolor sit amet, consectetur adipiscing elit, sed do eiusmod tempor incididunt ut labore et dolore magna aliqua. Ut enim ad minim veniam, quis nostrud exercitation ullamco laboris nisi ut aliquip ex ea commodo consequat.</p></div>
  <div class="foot-col abs" style="left:655px"><div class="foot-head">Usefull Links</div><ul><li>Home</li><li>About Us</li><li>Meet Our Dentiset</li><li>Contact Us</li><li>Terms &amp; Condition</li><li>Privacy Policy</li></ul></div>
  <div class="foot-col abs" style="left:918px"><div class="foot-head">Our Services</div><ul><li>Home</li><li>About Us</li><li>Meet Our Dentiset</li><li>Contact Us</li><li>Terms &amp; Condition</li><li>Privacy Policy</li></ul></div>
  <div class="foot-brand abs"><span class="brand-dot"></span><span class="brand-name">birch grove</span></div>
  <div class="foot-social abs"><span></span><span></span><span></span><span></span><span></span></div>
  <p class="copyright abs">Copyright © 2022 Birch Grove. All rights reserved.</p>
</footer>
</body>
</html>
```